Product Description Graphic

We are designing a new product and need a better graphic to describe it.

We are not worried about names of the modules yet but want to be descriptive of capabilities. Right now "Present & CMA" should really be "Presentations & CMA".

I overall like the shape of the triangle and the arrow for Contacts but this is a very unsophisticated graphic done by a non-designer. Also need to better show that each block of capabilites will also have paywall capabilities.

Target Market(s)

Real Estate Brokerage Firms and Real Estate Agents

Industry/Entity Type

Real Estate

Colors

Designer to choose colors to be used in the design.

Requirements
Must have
• Sophisticated design. Paywall description embedded.

```html
<!DOCTYPE html>
<html lang="en">
<head>
<meta charset="utf-8">
<title>Product Capabilities</title>
<link href="https://fonts.googleapis.com/css2?family=Nunito+Sans:wght@700;800&display=swap" rel="stylesheet">
<style>
  :root {
    --bg: #ffffff;
    --tier-email: #9cbdbc;
    --band-email: #7a9c93;
    --tier-present: #a9b6bc;
    --band-present: #878d8c;
    --contacts: #8fa6af;
    --contacts-stem: #adc3cc;
    --tier-web: #5f8f8a;
    --band-web: #4e6c68;
    --tier-mobile: #8a999d;
    --band-mobile: #6a7371;
    --hatch: #6b6680;
    --label: #ffffff;
    --ink: #111111;
  }
  html, body {
    margin: 0;
    width: 1200px;
    height: 1200px;
    overflow: hidden;
    background: var(--bg);
  }
  .diagram { display: block; width: 1200px; height: 1200px; }
  .module-label {
    font-family: "Nunito Sans", sans-serif;
    font-weight: 700;
    font-size: 17px;
    fill: var(--label);
  }
  .contacts-label {
    font-family: "Nunito Sans", sans-serif;
    font-weight: 800;
    font-size: 23px;
    fill: var(--label);
  }
  .legend-label {
    font-family: "Nunito Sans", sans-serif;
    font-weight: 800;
    font-size: 17px;
    fill: var(--ink);
  }
  .rounded { stroke-linejoin: round; stroke-width: 8; }
  .hatch-line { stroke: var(--hatch); stroke-width: 1; opacity: .6; }
</style>
</head>
<body>
<svg class="diagram" viewBox="0 0 1200 1200" xmlns="http://www.w3.org/2000/svg">
  <defs>
    <pattern id="paywall-hatch" width="22" height="22" patternUnits="userSpaceOnUse" patternTransform="rotate(-45)">
      <line class="hatch-line" x1="0" y1="0" x2="0" y2="22"/>
    </pattern>
  </defs>

  <!-- Email tier -->
  <g class="tier tier-email">
    <polygon class="rounded" points="597,334 666,452 486,746 326,746" fill="var(--tier-email)" stroke="var(--tier-email)"/>
    <polygon class="band" points="598,444 639,502 486,750 392,750" fill="var(--band-email)"/>
    <polygon points="597,334 666,452 486,746 326,746" fill="url(#paywall-hatch)"/>
    <text class="module-label" transform="translate(525,612) rotate(-56.8)" text-anchor="middle">
      <tspan x="0" y="-4">Email Nateure Print</tspan>
      <tspan x="0" y="17">&amp; Social</tspan>
    </text>
  </g>

  <!-- Presentations tier -->
  <g class="tier tier-present">
    <polygon class="rounded" points="676,468 859,746 692,746 600,584" fill="var(--tier-present)" stroke="var(--tier-present)"/>
    <polygon class="band" points="598,584 645,510 796,750 692,750" fill="var(--band-present)"/>
    <polygon points="676,468 859,746 692,746 600,584" fill="url(#paywall-hatch)"/>
    <text class="module-label" transform="translate(670,648) rotate(56.8)" text-anchor="middle">
      <tspan x="0" y="-4">Presentations</tspan>
      <tspan x="0" y="17">&amp; CMA</tspan>
    </text>
  </g>

  <!-- Contacts core -->
  <g class="core-contacts">
    <rect x="565" y="740" width="39" height="118" rx="4" fill="var(--contacts)"/>
    <rect x="565" y="810" width="39" height="48" rx="4" fill="var(--contacts-stem)"/>
    <polygon class="rounded" points="587,606 677,746 495,746" fill="var(--contacts)" stroke="var(--contacts)"/>
    <text class="contacts-label" x="586" y="737" text-anchor="middle">CONTACTS</text>
  </g>

  <!-- Websites tier -->
  <g class="tier tier-web">
    <polygon class="rounded" points="324,766 553,766 553,854 265,854" fill="var(--tier-web)" stroke="var(--tier-web)"/>
    <rect class="band" x="363" y="762" width="194" height="48" rx="10" fill="var(--band-web)"/>
    <polygon points="324,766 553,766 553,854 265,854" fill="url(#paywall-hatch)"/>
    <text class="module-label" x="391" y="792">Websites &amp; Leads</text>
  </g>

  <!-- Mobile tier -->
  <g class="tier tier-mobile">
    <polygon class="rounded" points="616,766 866,766 923,854 616,854" fill="var(--tier-mobile)" stroke="var(--tier-mobile)"/>
    <rect class="band" x="612" y="762" width="210" height="48" rx="10" fill="var(--band-mobile)"/>
    <polygon points="616,766 866,766 923,854 616,854" fill="url(#paywall-hatch)"/>
    <text class="module-label" x="631" y="792">Mobile</text>
  </g>

  <!-- Legend -->
  <g class="legend">
    <line class="hatch-line" x1="862" y1="380" x2="888" y2="406" style="opacity:1"/>
    <line class="hatch-line" x1="891" y1="380" x2="910" y2="399" style="opacity:1"/>
    <line class="hatch-line" x1="853" y1="402" x2="888" y2="437" style="opacity:1"/>
    <line class="hatch-line" x1="871" y1="398" x2="910" y2="437" style="opacity:1"/>
    <line class="hatch-line" x1="853" y1="430" x2="860" y2="437" style="opacity:1"/>
    <text class="legend-label" x="944" y="403">Paywall</text>
    <text class="legend-label" x="944" y="434">Feature</text>
  </g>
</svg>
</body>
</html>
```